Business Design for Printed Shipping Tape

We need a company logo design to be printed on packaging natural color WAT tape for shipping boxes. www.brightmeadowkelp.com
The tape is 3" wide. Repeat pattern every 10 inches.
Would like our website vertical at one end side and "The Future of Nutrition" on the opposite end.

Industry/Entity Type

Health, Nutrition

Font styles to use
Sans Serif

Requirements
Must have
• Company Logo (attached) website and text "The Future of Nutrition"
Nice to have
• Tape is Natural Color.

```html
<!DOCTYPE html>
<html lang="en">
<head>
<meta charset="utf-8">
<title>Bright Meadow Kelp – Shipping Tape</title>
<link rel="stylesheet" href="https://fonts.googleapis.com/css2?family=Poppins:ital,wght@0,500;0,700;1,900&display=swap">
<style>
  :root {
    --backdrop: #3b3b3d;
    --tape: #ffffff;
    --teal: #25a892;
    --ink: #333333;
  }
  * { margin: 0; padding: 0; box-sizing: border-box; }
  html, body {
    width: 1200px;
    height: 503px;
    overflow: hidden;
    background: var(--backdrop);
  }
  .canvas {
    position: relative;
    width: 1200px;
    height: 503px;
    background: var(--backdrop);
  }
  .tape {
    position: absolute;
    left: 129px;
    top: 110px;
    width: 942px;
    height: 283px;
    background: var(--tape);
    overflow: hidden;
  }
  .tape-wedge {
    position: absolute;
    left: 0;
    top: 0;
    width: 70px;
    height: 283px;
  }
  .brand {
    position: absolute;
    left: 92px;
    top: 65px;
    width: 300px;
    text-align: center;
  }
  .brand-dot {
    display: block;
    width: 46px;
    height: 46px;
    margin: 0 auto 10px;
    border-radius: 50%;
    background: var(--teal);
  }
  .brand-name {
    font-family: "Poppins", sans-serif;
    font-weight: 700;
    font-size: 35px;
    line-height: 42px;
    color: var(--ink);
    letter-spacing: -0.5px;
    text-transform: uppercase;
  }
  .headline {
    position: absolute;
    left: 420px;
    top: 50px;
    font-family: "Poppins", sans-serif;
    font-weight: 900;
    font-style: italic;
    font-size: 76px;
    line-height: 56px;
    letter-spacing: -2px;
    color: var(--teal);
    text-transform: uppercase;
  }
  .headline span { display: block; padding-top: 8px; }
  .website {
    position: absolute;
    left: 904px;
    top: 141px;
    transform: translate(-50%, -50%) rotate(-90deg);
    font-family: "Poppins", sans-serif;
    font-weight: 500;
    font-size: 14px;
    color: var(--ink);
    white-space: nowrap;
  }
</style>
</head>
<body>
  <main class="canvas">
    <section class="tape">
      <svg class="tape-wedge" viewBox="0 0 70 283" aria-hidden="true">
        <polygon points="0,0 70,0 19,283 0,283" fill="var(--teal)"/>
      </svg>

      <div class="brand">
        <span class="brand-dot" aria-hidden="true"></span>
        <p class="brand-name">Bright Meadow<br>Kelp</p>
      </div>

      <h1 class="headline">
        <span>The</span>
        <span>Future of</span>
        <span>Nutrition</span>
      </h1>

      <p class="website">www.brightmeadowkelp.com</p>
    </section>
  </main>
</body>
</html>
```